Website Home Page Main Banner Design (wholesale)

1170 x 547 PNG web banner design

Verano Global Corporation is a full-service importer based out of New York City, New York. For over 50 years, we have offered our customers fashionable, quality products at competitive prices. The company has a full in-house development and design staff, with a 100,000 sq. foot warehouse in Perth Amboy, New Jersey. Our talented design team, with extensive overseas sourcing experience, is always on the search for innovative ideas and hot new products.

Verano currently consists of the following divisions– Toddler Novelty Company (TNC), Hair Accessories, Jewelry (Gleamora), General Merchandise (Brandavex), Beauty Implements, Socks & Hosiery and Electronics.

Website- https://verano.quillbrook-hosting.com/index.php/

Target Market(s)

Retailers

Industry/Entity Type

Wholesale

Number of Pages Required

1 page

Font styles to use
Serif

Colors

Designer to choose colors to be used in the design.

Requirements
Must have
• Company Name- Verano Global Corp
Nice to have
• Some of the products featured on the site
Should not have
• Nothing

```html
<!DOCTYPE html>
<html lang="en">
<head>
<meta charset="utf-8">
<title>Verano Global Corp — Wholesale Fashion Accessories</title>
<link rel="stylesheet" href="https://fonts.googleapis.com/css2?family=PT+Sans:wght@400;700&display=swap">
<style>
:root{
  --ink:#222;
  --muted:#666;
  --dark:#2d2d2d;
  --darker:#262626;
  --accent:#3d40d0;
  --light:#ebebeb;
  --panel:#f7f6f6;
  --line:#e2e2e2;
  --white:#fff;
}
*{box-sizing:border-box;margin:0;padding:0}
html,body{width:693px;height:1200px;overflow:hidden;background:var(--white)}
body{font-family:"PT Sans",Arial,sans-serif;color:var(--ink);position:relative}
a{color:inherit;text-decoration:none}

.topbar{position:absolute;left:0;top:0;width:693px;height:24px;border-bottom:1px solid var(--line);font-size:7.5px;color:#444}
.topbar .item{position:absolute;top:8px;display:flex;align-items:center;gap:4px}
.topbar svg{width:7px;height:7px;fill:#333}

.header{position:absolute;left:0;top:24px;width:693px;height:67px}
.brand{position:absolute;left:57px;top:19px;font-size:19px;color:#111}
.search{position:absolute;left:205px;top:22px;width:297px;height:25px;border:1px solid #ddd;border-radius:13px;font-size:6.5px}
.search .cat{position:absolute;left:16px;top:8px;font-weight:700}
.search .caret{position:absolute;left:76px;top:7px;width:10px;height:10px;border:1px solid #ddd;border-radius:50%}
.search .field{position:absolute;left:100px;top:8px;color:#777}
.search .btn{position:absolute;right:-1px;top:-1px;width:59px;height:25px;border-radius:13px;background:var(--accent);color:var(--white);font-weight:700;text-align:center;line-height:25px}
.cart{position:absolute;left:537px;top:0;width:99px;height:67px;background:var(--light)}
.cart svg{position:absolute;left:8px;top:27px;width:19px;height:16px}
.cart .badge{position:absolute;left:22px;top:22px;width:10px;height:10px;border-radius:50%;background:var(--accent);color:var(--white);font-size:6.5px;text-align:center;line-height:10px}
.cart .label{position:absolute;left:37px;top:27px;font-size:6.5px;font-weight:700}
.cart .total{position:absolute;left:37px;top:36px;font-size:8.5px;font-weight:700;color:var(--accent)}

.nav{position:absolute;left:0;top:91px;width:693px;height:25px;background:var(--darker);color:#eee;font-size:7.5px}
.nav .home{position:absolute;left:57px;top:0;width:34px;height:25px;background:var(--accent)}
.nav .home svg{position:absolute;left:11px;top:7px;width:12px;height:11px;fill:var(--white)}
.nav ul{position:absolute;left:101px;top:9px;list-style:none;display:flex}
.nav li{padding:0 9.5px;border-left:1px solid #555;line-height:8px}
.nav li:first-child{border-left:0;padding-left:0}

.hero{position:absolute;left:0;top:116px;width:693px;height:270px;background:var(--light);overflow:hidden}
.hero svg.shape{position:absolute;left:0;top:0}
.hero h1{position:absolute;left:57px;top:153px;font-size:19px;line-height:28px;font-weight:700;color:var(--white);letter-spacing:.2px}
.hero .pitch{position:absolute;left:392px;top:99px;width:276px;text-align:center}
.hero .pitch h2{font-size:11.5px;line-height:16.5px;font-weight:700;color:#111;letter-spacing:.3px}
.hero .pitch p{margin-top:7px;font-size:10.3px;line-height:16px;color:#111;word-spacing:1px}

.grid{position:absolute;left:70px;top:414px;width:552px;display:grid;grid-template-columns:178px 176px 178px;grid-auto-rows:198px;column-gap:10px;row-gap:12px}
.card{background:var(--white);box-shadow:0 0 6px rgba(0,0,0,.06);position:relative}
.card .photo{position:absolute;left:18px;top:10px;right:18px;height:155px;border-radius:3px}
.card .name{position:absolute;left:0;right:0;top:172px;text-align:center;font-size:13.5px;color:#222}

.brands{position:absolute;left:0;top:848px;width:693px;text-align:center}
.brands h2{font-size:19.5px;font-weight:400;letter-spacing:.5px}
.carousel .arrow{position:absolute;top:88px;width:7px;height:11px}
.carousel .logo{position:absolute;top:52px;width:92px;height:88px;border-radius:4px}

.signup{position:absolute;left:0;top:1028px;width:693px;height:134px;background:var(--panel);text-align:center}
.signup h2{margin-top:30px;font-size:19.5px;font-weight:400;letter-spacing:.3px}
.signup p{margin-top:4px;font-size:5.6px;color:var(--muted);letter-spacing:.2px}
.signup .cta{display:block;margin:11px auto 0;width:203px;height:16px;background:var(--darker);color:var(--white);font-size:5.8px;font-weight:700;line-height:16px;border:1px solid #000}

.footer{position:absolute;left:0;top:1162px;width:693px;height:38px;background:var(--dark);color:var(--white);font-size:5.8px}
.footer ul{position:absolute;left:52px;top:16px;list-style:none;display:flex;gap:11px}
.footer .copy{position:absolute;right:48px;top:15px}
</style>
</head>
<body>

<div class="topbar">
  <span class="item" style="left:64px"><svg viewBox="0 0 10 10"><path d="M0 4h5V2l3 3-3 3V6H0zM6 0h4v10H6V9h3V1H6z"/></svg>Log In</span>
  <span class="item" style="left:111px"><svg viewBox="0 0 10 10"><path d="M1 1h5v1H2v6h6V5h1v4H1zM8 0l2 2-5 5H3V5z"/></svg>Register</span>
  <span class="item" style="left:428px"><svg viewBox="0 0 10 10"><circle cx="5" cy="3" r="2.5"/><path d="M0 10c0-3 2-4.5 5-4.5s5 1.5 5 4.5z"/></svg>My Account!</span>
  <span class="item" style="left:503px"><svg viewBox="0 0 10 10"><path d="M2 0h4l2 2v8H2zM3 4h4v1H3zm0 2h4v1H3z"/></svg>My Wishlist!</span>
  <span class="item" style="left:578px"><svg viewBox="0 0 10 10"><path d="M0 2h10v6H0zm1 1v4h8V3zm1 1h3v1H2z"/></svg>Checkout!</span>
</div>

<header class="header">
  <a class="brand" href="#">Verano</a>
  <div class="search">
    <span class="cat">All Categories</span>
    <span class="caret"></span>
    <span class="field">Search Product</span>
    <span class="btn">SEARCH</span>
  </div>
  <div class="cart">
    <svg viewBox="0 0 20 17"><path d="M0 0h4l1 3h15l-3 8H6L3 2H0z" fill="#111"/><circle cx="7" cy="15" r="1.8" fill="#111"/><circle cx="16" cy="15" r="1.8" fill="#111"/></svg>
    <span class="badge">0</span>
    <span class="label">SHOPPING CART</span>
    <span class="total">$0.00</span>
  </div>
</header>

<nav class="nav">
  <a class="home" href="#"><svg viewBox="0 0 12 11"><path d="M6 0l6 5.5h-2V11H7.5V7.5h-3V11H2V5.5H0z"/></svg></a>
  <ul>
    <li>About Us</li><li>Toddler Novelty Company</li><li>Hair Accessories</li><li>Jewelry</li><li>Socks</li><li>Hba</li><li>General Merchandise</li><li>Closeouts</li><li>Contact Us</li>
  </ul>
</nav>

<section class="hero">
  <svg class="shape" width="693" height="270" viewBox="0 0 693 270">
    <polygon points="0,0 348,0 378,142 348,270 0,270" fill="#c4c4c4"/>
    <polygon points="0,0 338,0 372,142 338,270 0,270" fill="#303030"/>
  </svg>
  <h1>VERANO GLOBAL CORP<br>FOUNDED IN 1961</h1>
  <div class="pitch">
    <h2>THE ONE-STOP-SHOP FOR RETAILERS IN<br>THE FASHION ACCESSORY INDUSTRY</h2>
    <p>Infant Specialty &nbsp;|&nbsp; Kids hair &nbsp;|&nbsp; Ladies Hair &nbsp;|&nbsp; Jewelry<br>General Merchandise &nbsp;|&nbsp; Kids Toys &nbsp;|&nbsp; Legwear &nbsp;|&nbsp; HBA</p>
  </div>
</section>

<main class="grid">
  <div class="card"><div class="photo" role="img" aria-label="Boxed baby gift set with pink and white caps and booties" style="background:linear-gradient(160deg,#f4e9ee,#f6c9d9 55%,#e9eef0)"></div><div class="name">Toddler Novelty Company</div></div>
  <div class="card"><div class="photo" role="img" aria-label="Carded pack of black and grey hair elastics" style="background:linear-gradient(180deg,#b9b9bc,#3a3a3c 40%,#222 80%,#d8d4cc)"></div><div class="name">Hair Accessories</div></div>
  <div class="card"><div class="photo" role="img" aria-label="Pair of silver statement drop earrings on a black card" style="background:linear-gradient(180deg,#2a2a2a 25%,#cfcfcf 40%,#8e8e8e 75%,#fff)"></div><div class="name">Jewelry</div></div>
  <div class="card"><div class="photo" role="img" aria-label="Striped novelty kids socks in black, white and green" style="background:linear-gradient(135deg,#f2f2f2,#3a3a3a 40%,#6fbf5a 55%,#e36aa2 65%,#f2f2f2)"></div><div class="name">Socks</div></div>
  <div class="card"><div class="photo" role="img" aria-label="Black travel toiletry bag with a red product card" style="background:linear-gradient(90deg,#3a3a3a 20%,#a32a2e 45%,#a32a2e 60%,#3a3a3a 80%)"></div><div class="name">HBA</div></div>
  <div class="card"><div class="photo" role="img" aria-label="Light blue baby gift bag with toy train print" style="background:linear-gradient(160deg,#d8ecf8,#a9d0ee 60%,#c8e2f4)"></div><div class="name">General Merchandise</div></div>
</main>

<section class="brands">
  <h2>Brands</h2>
  <div class="carousel">
    <svg class="arrow" style="left:90px" viewBox="0 0 7 11"><path d="M6 0.5L1 5.5l5 5" fill="none" stroke="#555" stroke-width="1.3"/></svg>
    <div class="logo" role="img" aria-label="Beauty implements: brush and nail clippers" style="left:114px;background:linear-gradient(90deg,#fff,#bdbdbd 30%,#222 45%,#c9c9c9 70%,#fff)"></div>
    <div class="logo" role="img" aria-label="Multicoloured patterned socks" style="left:218px;background:linear-gradient(120deg,#fff,#e4573d 30%,#f2b134 45%,#3ba39b 60%,#8a4fb0 75%,#fff)"></div>
    <div class="logo" role="img" aria-label="Open pink umbrella" style="left:354px;background:radial-gradient(ellipse at 50% 40%,#e23fc4,#ef6fd8 55%,#fff 75%)"></div>
    <div class="logo" role="img" aria-label="Beauty implements: brush and nail clippers" style="left:494px;background:linear-gradient(90deg,#fff,#bdbdbd 30%,#222 45%,#c9c9c9 70%,#fff)"></div>
    <svg class="arrow" style="left:596px" viewBox="0 0 7 11"><path d="M1 0.5l5 5-5 5" fill="none" stroke="#555" stroke-width="1.3"/></svg>
  </div>
</section>

<section class="signup">
  <h2>Create an Account</h2>
  <p>IN ORDER TO MAKE A PURCHASE, PLEASE SIGN UP FOR AN ACCOUNT</p>
  <a class="cta" href="#">SIGN UP FOR AN ACCOUNT TO MAKE A PURCHASE</a>
</section>

<footer class="footer">
  <ul>
    <li>Toddler Novelty Company</li><li>Hair Accessories</li><li>Jewelry</li><li>Socks</li><li>HBA</li><li>General Merchandise</li><li>Closeouts</li>
  </ul>
  <span class="copy">Copyright 2017 Verano Global.</span>
</footer>

</body>
</html>
```